new Ridgeway Bug Shield Flyer 8.5"x11"

We need a new flyer for our pest control company. We need it to be themed like our truck wrap. We have also attached is our old flyer.
The Best Defense is a Great Offense. Our Bug Guns are Locked, Loaded and Ready for action!
Don't be caught defenseless, Call Ridgeway Bug Shield today!!
"The Solution to your bug pollution"
www.ridgewaybugshield.com
352-481-6037

add a 10% off coupon code for existing Ridgeway Home Inspections customers

Target Market(s)

Home owners

Industry/Entity Type

Pest Control

Requirements
Must have
• our theme like our truck wrap

```html
<!DOCTYPE html>
<html lang="en">
<head>
<meta charset="utf-8">
<title>Ridgeway Bug Shield Flyer</title>
<link href="https://fonts.googleapis.com/css2?family=Black+Ops+One&family=Didact+Gothic&family=Questrial&family=Oswald:wght@500;700&display=swap" rel="stylesheet">
<style>
  :root {
    --camo-light: #cfc7ab;
    --camo-dark: #a9a284;
    --panel: #e2e9df;
    --roof: #8d9197;
    --brand-red: #c4232b;
    --brand-blue: #1f4e8c;
    --ink: #3b3b3b;
    --white: #ffffff;
  }
  * { margin: 0; padding: 0; box-sizing: border-box; }
  html, body { width: 998px; height: 1200px; overflow: hidden; background: #fff; }
  .flyer { position: relative; width: 998px; height: 1200px; overflow: hidden; font-family: "Questrial", sans-serif; color: var(--ink); }
  .flyer-backdrop { position: absolute; inset: 0; }
  .brand-mark { position: absolute; left: 40px; top: 70px; display: flex; align-items: center; gap: 10px; white-space: nowrap; }
  .brand-mark .dot { width: 24px; height: 24px; border-radius: 50%; background: var(--brand-blue); flex: none; }
  .brand-mark .name { font-family: "Questrial", sans-serif; font-size: 22px; color: var(--ink); }
  .headline { position: absolute; left: 60px; width: 998px; text-align: center; font-family: "Black Ops One", sans-serif; font-weight: 400; }
  .headline.top { top: 268px; font-size: 64px; color: var(--brand-red); }
  .headline.main { top: 350px; font-size: 80px; color: var(--brand-blue); }
  .tagline { position: absolute; top: 490px; left: 110px; width: 900px; text-align: center; font-family: "Didact Gothic", sans-serif; font-size: 38px; line-height: 1.3; color: var(--ink); }
  .tagline .caps { text-transform: uppercase; font-weight: 700; }
  .soldier-photo { position: absolute; left: 50px; top: 540px; width: 270px; height: 400px; border-radius: 40px 40px 0 0; background: linear-gradient(170deg, #a28b68, #6b5b45 55%, #3d3a33); }
  .pitch { position: absolute; top: 630px; left: 340px; width: 440px; text-align: center; font-family: "Didact Gothic", sans-serif; font-weight: 700; font-size: 23px; line-height: 1.42; color: #222; }
  .call-to-arms { position: absolute; top: 752px; left: 340px; width: 440px; text-align: center; font-family: "Black Ops One", sans-serif; color: var(--brand-red); font-size: 42px; line-height: 1.3; }
  .roach-art { position: absolute; left: 735px; top: 720px; width: 225px; height: 330px; border-radius: 45%; background: radial-gradient(circle at 45% 45%, #b97a4b, #7a4a2a 70%); }
  .contact { position: absolute; top: 930px; left: 380px; width: 360px; text-align: center; }
  .contact .warning { font-size: 20px; color: var(--brand-blue); font-weight: 700; }
  .contact .urge { font-size: 19px; color: var(--brand-red); font-weight: 700; text-transform: uppercase; }
  .contact .phone { margin-top: 8px; display: flex; justify-content: center; align-items: center; gap: 10px; font-family: "Oswald", sans-serif; font-weight: 500; font-size: 34px; line-height: 44px; color: var(--brand-blue); }
  .website { position: absolute; top: 1102px; left: 370px; width: 380px; text-align: center; color: var(--white); font-size: 17px; letter-spacing: 4px; }
  .coupon { position: absolute; left: 92px; top: 915px; width: 240px; height: 245px; }
  .coupon-text { position: absolute; left: 92px; top: 935px; width: 240px; text-align: center; color: var(--white); }
  .coupon-text .deal { display: block; margin: 30px auto 0; width: 236px; background: var(--white); color: var(--brand-red); font-family: "Oswald", sans-serif; font-weight: 700; font-size: 32px; line-height: 46px; }
  .coupon-text .terms { display: block; margin-top: 14px; font-size: 18px; line-height: 1.25; padding: 0 24px; }
</style>
</head>
<body>
<main class="flyer">
  <svg class="flyer-backdrop" width="998" height="1200" viewBox="0 0 998 1200" aria-hidden="true">
    <defs>
      <linearGradient id="camo" x1="0" y1="0" x2="1" y2="1">
        <stop offset="0" stop-color="#cfc7ab"/>
        <stop offset="1" stop-color="#a9a284"/>
      </linearGradient>
      <linearGradient id="metal" x1="0" y1="0" x2="1" y2="0">
        <stop offset="0" stop-color="#b9bcc1"/>
        <stop offset="0.5" stop-color="#8f9398"/>
        <stop offset="1" stop-color="#6e7278"/>
      </linearGradient>
      <linearGradient id="coupon-fill" x1="0" y1="0" x2="0" y2="1">
        <stop offset="0" stop-color="#f59b1c"/>
        <stop offset="1" stop-color="#d9271d"/>
      </linearGradient>
    </defs>
    <rect width="998" height="1200" fill="url(#camo)"/>
    <rect y="860" width="998" height="340" fill="url(#metal)"/>
    <path d="M30 450 L455 175 L570 250 L570 90 L712 90 L712 330 L968 440 L968 900 Q500 1230 30 900 Z"
          fill="#e2e9df" stroke="#8d9197" stroke-width="26" stroke-linejoin="miter"/>
    <path d="M42 905 Q500 1218 956 905" fill="none" stroke="#1f4e8c" stroke-width="5"/>
  </svg>

  <div class="brand-mark">
    <span class="dot"></span>
    <span class="name">Ridgeway Bug Shield</span>
  </div>

  <h1 class="headline top">RIDGEWAY</h1>
  <h1 class="headline main">BUG SHIELD</h1>

  <p class="tagline"><span class="caps">The Solution</span><br>to your bug pollution</p>

  <div class="soldier-photo" role="img" aria-label="Photo of an armed soldier in camouflage gear"></div>

  <p class="pitch">The Best Defense is a Great Offense.<br>Our Bug Guns are Locked,<br>Loaded and</p>
  <p class="call-to-arms">READY FOR<br>ACTION</p>

  <div class="roach-art" role="img" aria-label="Cartoon cockroach waving a white flag inside a red crosshair"></div>

  <div class="contact">
    <p class="warning">Don't be caught defenseless</p>
    <p class="urge">Call us today!!</p>
    <p class="phone">
      <svg width="30" height="30" viewBox="0 0 32 32" aria-hidden="true">
        <circle cx="16" cy="16" r="14" fill="none" stroke="#222" stroke-width="2"/>
        <path d="M11 9 l3 0 l1.5 4 l-2 1.5 q1.5 3.5 4 5 l1.5 -2 l4 1.5 l0 3 q-8 1 -12 -13 z" fill="#222"/>
      </svg>
      352-481-6037
    </p>
  </div>

  <p class="website">www.ridgewaybugshield.com</p>

  <svg class="coupon" viewBox="0 0 240 245" aria-hidden="true">
    <path d="M120 5 L232 50 L225 165 Q200 215 120 240 Q40 215 15 165 L8 50 Z" fill="#ffffff"/>
    <path d="M120 16 L221 57 L214 162 Q192 205 120 228 Q48 205 26 162 L19 57 Z" fill="url(#coupon-fill)"/>
  </svg>
  <div class="coupon-text">
    <span class="deal">10% OFF</span>
    <span class="terms">for existing Ridgeway Home Inspections customers</span>
  </div>
</main>
</body>
</html>
```